Sexy Cover-Design für erotischen Liebesroman gesucht
Der Designer ist sehr gut auf meine Wünsche eingegangen und war im Umgang auch sehr nett und immer gut gelaunt. Seine Arbeit erledigt er zügig und zuverlässig.
Zielgruppe
Mein Roman ist ein erotischer Liebesroman ab 18 und spielt in Montana. Im Mittelpunkt steht die Liebesgeschichte einer 36-jährigen Hamburgerin und eines 39-jährigen Cowboys, der sich gezwungenermaßen mit Kampfsport beschäftigt. Meine Zielgruppe sind Frauen, die es gerne heiß mögen.
Aufgabenstellung
Da in meinem Buch explizite erotische Szenen vorkommen, darf das Cover ruhig auch sexy sein.
(Veltora Stock DATEI-NR.: 503917248 erscheint mir sehr passend, nur um ein Beispiel zu nennen). Muss aber nicht, der Kreativität sind natürlich keine Grenzen gesetzt.

```html
<!DOCTYPE html>
<html lang="de">
<head>
<meta charset="utf-8">
<title>Mein heißer Sommer – Umschlag</title>
<link rel="stylesheet" href="https://fonts.googleapis.com/css2?family=Catamaran:wght@300;400;600&family=Parisienne&display=swap">
<style>
  :root {
    --bg: #14110d;
    --panel: #000000;
    --frame: #1e8fd0;
    --text: #f2f2f2;
    --feather-box: #e9eaee;
    --badge: #5a5a5a;
    --sepia-light: #b9ad8c;
    --sepia-mid: #6e644c;
    --sepia-dark: #221d15;
  }
  html, body {
    margin: 0;
    padding: 0;
    width: 1200px;
    height: 851px;
    overflow: hidden;
    background: var(--bg);
  }
  .cover-wrap {
    position: relative;
    width: 1200px;
    height: 851px;
    background: var(--bg);
    overflow: hidden;
    font-family: "Catamaran", sans-serif;
    color: var(--text);
  }

  /* Back cover */
  .blurb-box {
    position: absolute;
    left: 93px;
    top: 105px;
    width: 376px;
    height: 553px;
    box-sizing: border-box;
    border: 1px solid var(--frame);
    background: var(--panel);
    padding: 18px 17px 0 18px;
  }
  .blurb-box p {
    margin: 0;
    font-size: 13.2px;
    font-weight: 300;
    line-height: 21px;
    text-align: justify;
    hyphens: manual;
  }
  .blurb-box strong { font-weight: 600; }
  .feather-spacer {
    float: left;
    width: 77px;
    height: 126px;
  }
  .feather-art {
    position: absolute;
    left: 64px;
    top: 78px;
    width: 118px;
    height: 168px;
    background: var(--feather-box);
  }

  /* Spine */
  .spine-badge {
    position: absolute;
    left: 564px;
    top: 32px;
    width: 72px;
    height: 72px;
  }
  .spine-title {
    position: absolute;
    left: 601px;
    top: 512px;
    transform: translate(-50%, -50%) rotate(-90deg);
    white-space: nowrap;
    font-family: "Parisienne", cursive;
    font-size: 64px;
    line-height: 1;
    color: var(--text);
  }
  .spine-author {
    position: absolute;
    left: 560px;
    top: 760px;
    width: 82px;
    text-align: center;
    font-size: 20px;
    line-height: 21px;
    font-weight: 400;
  }

  /* Front cover */
  .front-photo {
    position: absolute;
    left: 655px;
    top: 0;
    width: 545px;
    height: 851px;
    background:
      radial-gradient(ellipse 55% 40% at 70% 12%, rgba(150,135,100,0.75), transparent 70%),
      radial-gradient(ellipse 50% 48% at 60% 50%, var(--sepia-light), var(--sepia-mid) 45%, transparent 80%),
      radial-gradient(ellipse 45% 30% at 65% 92%, rgba(90,85,75,0.8), transparent 75%),
      linear-gradient(90deg, var(--bg) 0%, var(--sepia-dark) 25%, var(--sepia-dark) 80%, var(--bg) 100%);
  }
  .front-title {
    margin: 0;
    font-weight: 400;
    font-family: "Parisienne", cursive;
    color: #ffffff;
    line-height: 1;
    white-space: nowrap;
  }
  .front-title span { position: absolute; }
  .front-title .word-mein { left: 682px; top: 410px; font-size: 92px; }
  .front-title .word-heisser { left: 822px; top: 478px; font-size: 86px; }
  .front-title .word-sommer { left: 698px; top: 560px; font-size: 92px; }
  .front-badge {
    position: absolute;
    left: 723px;
    top: 760px;
    width: 74px;
    height: 74px;
    opacity: 0.55;
  }
  .front-author {
    position: absolute;
    left: 1043px;
    top: 798px;
    font-size: 21px;
    font-weight: 400;
    color: #ffffff;
    white-space: nowrap;
  }
</style>
</head>
<body>
<div class="cover-wrap">

  <section class="back-cover">
    <div class="blurb-box">
      <div class="feather-spacer"></div>
      <p>Jeder kann sein Leben meistern und in den Griff bekommen um seine persönlichen Ziele erreichen. Ein entscheidendes Element ist immer wieder die Fähigkeit zur Selbstmotivation. Nie war diese so gefragt wie heute. Doch geht die in diesem Buch angesprochene Selbstmotivation weiter als allge&shy;mein gefordert.</p>
      <p>Selbstmotivation können wir leicht erlernen und zu unserem ganz persönlichen Vorankommen nutzen.</p>
      <p>In einem in dieser Form einzigartigen, vierstufigen Konzept zeigt der Autor einen mit Lebensfreude begleiteten Weg auf, um die eigene Selbstmotivation zu wecken und auszubauen. Dabei ist die Lebensfreude ein wichtiger Erfolgsfaktor.</p>
      <p>Einmal dieses wegweisende Konzept kennengelernt, entwickelt sich daraus eine ganz besondere Energie: "Die Dynamik der Selbstmotivation!" Damit erhält der Leser seinen persönlichen Schlüssel zu seinem Lebensglück.</p>
      <p>Unterstützt und begleitet wird dieses Konzept von fünfzig aus&shy;gewählten Übungen. Zusammengefasst in einem Arbeitsheft können sie bei Bedarf zusätzlich zum Ausdrucken herunterge&shy;laden werden.</p>
      <p>Mit den Webseiten <strong>www.antrieb7.de</strong> und <strong>www.die-kleine-dosis-schwung.de</strong>, sowie seinen Taschenbüchern und E-Books, hat sich Jonas Reiter als Blogger und Autor, ganz dem Thema Selbstmotivation verschrieben.</p>
    </div>
    <div class="feather-art" role="img" aria-label="Zeichnung einer Schreibfeder auf hellgrauem Feld"></div>
  </section>

  <section class="spine">
    <svg class="spine-badge" viewBox="0 0 72 72" role="img" aria-label="Altersangabe ab 18">
      <circle cx="36" cy="36" r="33" fill="none" stroke="var(--badge)" stroke-width="4"/>
      <text x="36" y="36" transform="rotate(-90 36 36)" text-anchor="middle" dominant-baseline="central" font-family="Catamaran, sans-serif" font-size="26" fill="var(--badge)">18+</text>
    </svg>
    <div class="spine-title">Mein heißer Sommer</div>
    <div class="spine-author">Miss<br>Holly<br>Vane</div>
  </section>

  <section class="front-cover">
    <div class="front-photo" role="img" aria-label="Sepiafoto: Oberkörper eines Mannes mit Strohhut und Jeans vor dunklem Hintergrund"></div>
    <h1 class="front-title" aria-label="Mein heißer Sommer">
      <span class="word-mein">Mein</span>
      <span class="word-heisser">heißer</span>
      <span class="word-sommer">Sommer</span>
    </h1>
    <svg class="front-badge" viewBox="0 0 74 74" role="img" aria-label="Altersangabe ab 18">
      <circle cx="37" cy="37" r="34" fill="none" stroke="#d8d2c2" stroke-width="3"/>
      <text x="37" y="38" text-anchor="middle" dominant-baseline="central" font-family="Catamaran, sans-serif" font-size="26" fill="#d8d2c2">18+</text>
    </svg>
    <div class="front-author">Miss Holly Vane</div>
  </section>

</div>
</body>
</html>
```